Orlent Telecom Business Card Competition

High quality international communications for consumers and business. We are re-designing our website and re-branding. Our current (old) website can be viewed at www.tryorlent.example Vision statement - We enable people and communities to build and maintain strong and lasting global connections This is the brand image that we are trying to get across: •Quality—Orlent delivers the highest quality connections wherever you need to communicate. •Service—Orlent is always there for you, with the industry-leading service that promises to ensure that every experience is a good one. •Value—Orlent provides the best value in the global communications market. Typical messaging: Connecting the Most Important People in the World. Focus on international communications

We want to convey our service quality and that we really care about the service we provide and our customers. We want to emphasis the international aspect of our business. We want to make it personal, but it has to relate to business as well as individuals. We want the card to be unique in design but clear enough to read. We want a business prospect as well as a regular person to look at our card and know what we do.

Target Market(s)

Consumer - multi-ethnic consumer base living in the US calling, texting and connecting with family and friends in countries around the world 2. Busine

Industry/Entity Type

Communications

Requirements
Must have
• 1. Logo must be visible (see uploaded)

2.Artist can use variations of our company colors to accent our logo:

Hex Codes:
Magenta = ab3179
Blue = 2895c0
Green = 8ebb3f

3.Must have the following slogan visible: Because Call Quality Counts

below are the required data fields:

Full Name: Mark Pellow
Position: Chief Financial Officer
Office: +1 571-482-3096 ext.214
Mobile: +1 571-482-3096
Fax: +1 571-482-3096
Email: MarkP@tryorlent.example
URL: www.tryorlent.example
Address:
31872 Wrenfield Lane
suite 408
Larkmont, VA 22914
USA

Nice to have
• Die cut cards or uniquely shaped cards would be interesting to see but not required

```html
<!DOCTYPE html>
<html lang="en">
<head>
<meta charset="utf-8">
<title>Orlent Telecom – Business Card</title>
<link rel="stylesheet" href="https://fonts.googleapis.com/css2?family=Arimo&family=Didact+Gothic&family=Fredoka:wght@500;600&display=swap">
<style>
  :root {
    --blue: #2895c0;
    --magenta: #ab3179;
    --green: #8ebb3f;
    --stock: #e8e5d8;
    --grey: #a7a7aa;
    --ink: #111111;
    --white: #ffffff;
  }
  html, body {
    margin: 0;
    padding: 0;
    width: 1200px;
    height: 1000px;
    overflow: hidden;
    background: var(--white);
  }
  .sheet {
    position: relative;
    width: 1200px;
    height: 1000px;
  }
  .card-art {
    position: absolute;
    left: 0;
    top: 0;
    width: 1200px;
    height: 1000px;
  }
  .card-shape {
    fill: var(--stock);
    filter: drop-shadow(7px 6px 3px rgba(0, 0, 0, 0.38));
  }
  .label {
    font-family: "Didact Gothic", sans-serif;
    fill: var(--white);
    opacity: 0.85;
    letter-spacing: 1px;
  }
  .value {
    font-family: "Fredoka", sans-serif;
    font-weight: 500;
    fill: var(--white);
    letter-spacing: 0.6px;
  }
  .section-title {
    font-family: "Fredoka", sans-serif;
    font-weight: 600;
    font-size: 24px;
  }
  .section-title.contact { fill: var(--magenta); }
  .section-title.address { fill: var(--green); }
  .brand-name {
    font-family: "Fredoka", sans-serif;
    font-weight: 600;
    font-size: 42px;
    fill: var(--blue);
  }
  .palette {
    position: absolute;
    left: 958px;
    top: 866px;
  }
  .palette-title {
    margin: 0 0 22px;
    font-family: "Arimo", sans-serif;
    font-size: 20px;
    font-weight: 400;
    color: var(--ink);
    letter-spacing: 0.2px;
  }
  .swatches {
    display: flex;
    gap: 8px;
  }
  .swatch {
    width: 34px;
    height: 34px;
  }
  .swatch.blue { background: var(--blue); }
  .swatch.magenta { background: var(--magenta); }
  .swatch.green { background: var(--green); }
  .swatch.stock { background: var(--stock); }
  .swatch.grey { background: var(--grey); }
</style>
</head>
<body>
<main class="sheet">
  <svg class="card-art" viewBox="0 0 1200 1000" xmlns="http://www.w3.org/2000/svg">
    <defs>
      <clipPath id="front-clip">
        <path d="M70,145 A123,123 0 0 1 193,22 L870,22 L870,355 A123,123 0 0 1 747,478 L70,478 Z"/>
      </clipPath>
    </defs>

    <g class="card-front">
      <path class="card-shape" d="M70,145 A123,123 0 0 1 193,22 L870,22 L870,355 A123,123 0 0 1 747,478 L70,478 Z"/>

      <g clip-path="url(#front-clip)">
        <path fill="var(--blue)" d="M363,45 L743,45 Q753,45 753,55 L753,118 L782,134 L363,135 Q353,135 353,125 L353,55 Q353,45 363,45 Z"/>
        <text class="label" x="376" y="78" font-size="20">Full Name</text>
        <text class="label" x="486" y="78" font-size="16">:</text>
        <text class="value" x="505" y="79" font-size="21">Mark Pellow</text>
        <text class="label" x="376" y="114" font-size="20">Position</text>
        <text class="label" x="486" y="114" font-size="16">:</text>
        <text class="value" x="507" y="115" font-size="21">Chief Financial Officer</text>

        <path role="img" aria-label="Profile icon" fill="var(--blue)" d="M786,105 A22,24 0 1 1 830,105 A22,24 0 1 1 786,105 Z M765,173 A43,40 0 0 1 851,173 Z"/>

        <g transform="rotate(-14 141 229)">
          <rect x="126" y="208" width="30" height="42" rx="5" fill="var(--magenta)"/>
          <rect x="131" y="214" width="20" height="26" rx="1.5" fill="var(--stock)"/>
          <circle cx="141" cy="245" r="2.2" fill="var(--stock)"/>
        </g>
        <text class="section-title contact" x="172" y="250">Contact</text>

        <path fill="var(--magenta)" d="M69,264 L600,264 L600,406 A25,25 0 0 1 575,431 L69,431 Z"/>
        <g class="contact-rows">
          <text class="label" x="127" y="304" font-size="18">Office</text>
          <text class="label" x="127" y="330" font-size="18">Mobile</text>
          <text class="label" x="127" y="356" font-size="18">Fax</text>
          <text class="label" x="127" y="383" font-size="18">Email</text>
          <text class="label" x="127" y="409" font-size="18">URL</text>
          <text class="label" x="257" y="304" font-size="12">:</text>
          <text class="label" x="257" y="330" font-size="12">:</text>
          <text class="label" x="257" y="356" font-size="12">:</text>
          <text class="label" x="257" y="383" font-size="12">:</text>
          <text class="label" x="257" y="409" font-size="12">:</text>
          <text class="value" x="285" y="305" font-size="20" xml:space="preserve">+1 571-482-3096  ext.214</text>
          <text class="value" x="285" y="331" font-size="20">+1 571-482-3096</text>
          <text class="value" x="285" y="357" font-size="20">+1 571-482-3096</text>
          <text class="value" x="285" y="384" font-size="20">MarkP@tryorlent.example</text>
          <text class="value" x="285" y="410" font-size="20">www.tryorlent.example</text>
        </g>

        <path fill="var(--green)" d="M652,252 L642,231 A12,12 0 1 1 663,231 Z"/>
        <circle cx="652.5" cy="225" r="4" fill="var(--stock)"/>
        <text class="section-title address" x="680" y="250">Address</text>

        <path fill="var(--green)" d="M672,264 L880,264 L880,431 L622,431 L622,314 A50,50 0 0 1 672,264 Z"/>
        <text class="value" x="649" y="304" font-size="19">31872 Wrenfield Lane</text>
        <text class="value" x="649" y="333" font-size="19">suite 408</text>
        <text class="value" x="649" y="362" font-size="19">Larkmont, VA 22914</text>
        <text class="value" x="649" y="391" font-size="19">USA</text>
      </g>
    </g>

    <g class="card-back">
      <path class="card-shape" d="M82,502 L757,502 A123,123 0 0 1 880,625 L880,957 L205,957 A123,123 0 0 1 82,834 Z"/>
      <rect x="335" y="698" width="40" height="40" rx="6" fill="var(--magenta)"/>
      <text class="brand-name" x="388" y="734">Orlent Telecom</text>
    </g>
  </svg>

  <section class="palette">
    <h2 class="palette-title">COLOURS APPLIED</h2>
    <div class="swatches">
      <div class="swatch blue"></div>
      <div class="swatch magenta"></div>
      <div class="swatch green"></div>
      <div class="swatch stock"></div>
      <div class="swatch grey"></div>
    </div>
  </section>
</main>
</body>
</html>
```